Verpackungsdesign für Ohrkerze
Zielgruppe
Hygiene ( Ohren )
Aufgabenstellung
Wir wollen ein Produkt anbieten für die Ohrhygiene ( Ohrenkerzen ) . Der Kunde soll sich beim Anblick der Verpackung direkt wohlfühlen. Und dabei das Gefühl haben das es sich um ein hochwertiges natürliches Produkt von einem vertrauenwürdigen Hersteller handelt. Das Logo 'VelroMist' sollte mit Gesundheit und ein wohlfühlfaktor verbunden sein. Das Logo soll vorne auf der Verpackung abgedruckt sein. Desweiteren sollte die Ohrenkerze auch mit abgebildet werden. Den Rest überlassen wir euch ;)
Das zweite Bild mit den Ohrenkerzen ist unser Produkt
Unser Produkt besteht aus Bienenwachs. Düfte sind verschiedene Rose,Sandelholz,Lavendel, Ätherische Öle das kann man ja individuell ändern auf der Verpackung als Schriftzug
Verpackungsmaße ca H:25cm B: 6cm T: 2,5
ANMERKUNG: Die Ohrenkerze ist kein muss mit abzubilden :)

```html
<!DOCTYPE html>
<html lang="de">
<head>
<meta charset="utf-8">
<title>VelroMist Ohrenkerzen – Verpackungsvarianten</title>
<link href="https://fonts.googleapis.com/css2?family=Marcellus&family=Tenor+Sans&family=Open+Sans:wght@400;600&display=swap" rel="stylesheet">
<style>
  :root{
    --gold-dark:#a87b52;
    --gold-light:#dcb891;
    --gold:#c49a70;
    --cream:#fbf4e4;
    --rose:#e3187a;
    --rose-deep:#d41773;
    --lavender:#62237f;
    --lavender-deep:#5a2c86;
    --sandal:#8c5b35;
    --sandal-deep:#6b4428;
    --white:#ffffff;
    --black:#0b0b0b;
    --page:#ffffff;
  }
  *{box-sizing:border-box;margin:0;padding:0}
  html,body{width:1023px;height:1200px;overflow:hidden;background:var(--page)}
  .sheet{position:relative;width:1023px;height:1200px}
  .pack{position:absolute;width:105px;height:440px;overflow:hidden;background:var(--tone);
        box-shadow:0 1px 2px rgba(0,0,0,.18)}
  .pack.rose{--tone:var(--rose);--accent:var(--rose)}
  .pack.lavender{--tone:var(--lavender);--accent:var(--lavender)}
  .pack.sandal{--tone:var(--sandal);--accent:var(--sandal)}
  .pack--textured.rose{--tone:var(--rose-deep)}
  .pack--textured.lavender{--tone:var(--lavender-deep)}
  .pack--textured.sandal{--tone:var(--sandal-deep)}
  .pack--textured{background:repeating-linear-gradient(90deg,rgba(255,255,255,.05) 0 1px,transparent 1px 3px),var(--tone)}
  .pack--cream{background:var(--cream)}
  .pack--cream.sandal{--accent:#5a3a22}

  .gold{background:linear-gradient(180deg,var(--gold-light),var(--gold-dark))}
  .header{position:absolute;left:0;top:0;width:100%;height:36px;display:flex;align-items:center;justify-content:center;gap:5px}
  .brand{display:flex;align-items:center;justify-content:center;gap:5px;font-family:"Marcellus",serif;font-size:13.5px;letter-spacing:.3px;color:var(--white)}
  .brand-dot{width:12px;height:12px;border-radius:50%;background:var(--white);flex:none}
  .brand--dark{color:#4a3a2c}
  .brand--dark .brand-dot{background:var(--gold)}
  .cream-brand{position:absolute;top:21px;left:0;width:100%}

  .strip-bottom{position:absolute;left:0;bottom:0;width:100%;height:8px}
  .strip-top{position:absolute;left:0;top:0;width:100%;height:6px}

  .tags{position:absolute;left:9px;top:88px;width:88px;list-style:none}
  .tags li{height:11px;margin-bottom:3px;background:var(--gold);color:var(--white);
           font-family:"Open Sans",sans-serif;font-size:6.6px;letter-spacing:.8px;line-height:11px;padding-left:6px}
  .tags li::before{content:"• "}

  .ritual{position:absolute;left:9px;top:103px;width:88px;height:48px;background:var(--black);border-radius:2px;overflow:hidden}
  .ritual-title{height:12px;background:var(--gold);color:var(--white);font-family:"Tenor Sans",sans-serif;font-size:8.2px;letter-spacing:.4px;text-align:center;line-height:12px}
  .ritual ul{list-style:none;padding:2px 0 0 8px;font-family:"Tenor Sans",sans-serif;font-size:8.4px;letter-spacing:.6px;line-height:10px;color:var(--white)}
  .ritual li::before{content:"· "}
  .pack--cream .ritual{background:var(--white);border:1px solid var(--accent);top:102px;height:50px}
  .pack--cream .ritual-title{background:var(--accent)}
  .pack--cream .ritual ul{color:var(--accent)}

  .medal{position:absolute;width:62px;height:62px;border-radius:50%;
         background:radial-gradient(circle at 38% 32%,#e3c3a0,#b88a5f 70%,#9c6f48);
         box-shadow:0 1px 3px rgba(0,0,0,.3);
         display:flex;align-items:center;justify-content:center;text-align:center;
         font-family:"Open Sans",sans-serif;font-weight:600;font-size:9.4px;line-height:12.5px;color:var(--white)}
  .pack--tone .medal{left:21px;top:282px}
  .pack--cream .medal{left:47px;top:163px}

  .product{position:absolute;left:0;width:100%;text-align:center;font-family:"Tenor Sans",sans-serif;color:var(--white)}
  .product-line{top:358px;font-size:12.6px;line-height:16px}
  .tagline{position:absolute;left:0;top:399px;width:100%;text-align:center;font-family:"Open Sans",sans-serif;font-size:5.4px;line-height:10px;color:rgba(255,255,255,.85)}

  .cream-title{position:absolute;left:0;width:100%;text-align:center;font-family:"Tenor Sans",sans-serif}
  .cream-title .kind{display:block;color:var(--gold);font-size:14px;line-height:19px}
  .cream-title .scent{display:block;color:var(--accent);font-size:12.5px;line-height:19px;letter-spacing:.5px}
  .pack--cream.classic .cream-title{top:53px}
  .pack--cream.modern .cream-title{top:55px}

  .photo{position:absolute;left:0;top:158px;width:100%;height:264px}
  .photo.rose-photo{background:linear-gradient(180deg,#efe0d8 0%,#e58fb4 25%,#e46ea5 55%,#d64f8d 85%,#8fa070 100%)}
  .photo.lavender-photo{background:linear-gradient(180deg,#e9e3df 0%,#a591b8 25%,#7c68a0 55%,#6a6f72 80%,#5d7a4f 100%)}
  .photo.sandal-photo{background:linear-gradient(180deg,#efe6db 0%,#6a4a34 28%,#3b2a20 55%,#7a4a2e 80%,#4a3022 100%)}
  .footer{position:absolute;left:0;bottom:0;width:100%;height:18px;color:var(--white);
          font-family:"Open Sans",sans-serif;font-size:6.8px;letter-spacing:.8px;line-height:18px;text-align:center}
</style>
</head>
<body>
<main class="sheet">

  <!-- Reihe 1: klassische Farbvariante -->
  <section class="pack pack--tone rose" style="left:87px;top:105px">
    <div class="header gold"><span class="brand"><span class="brand-dot"></span>VelroMist</span></div>
    <ul class="tags"><li>ENTSPANNEND</li><li>BESINNLICH</li><li>BERUHIGEND</li></ul>
    <div class="medal">MIT<br>BIENEN-<br>WACHS</div>
    <p class="product product-line">Ohrenkerzen<br>ROSE</p>
    <p class="tagline">Sinnliche Düfte für Harmonie<br>und Deine Entspannung</p>
    <div class="strip-bottom gold"></div>
  </section>
  <section class="pack pack--tone lavender" style="left:228px;top:105px">
    <div class="header gold"><span class="brand"><span class="brand-dot"></span>VelroMist</span></div>
    <ul class="tags"><li>ENTSPANNEND</li><li>BESINNLICH</li><li>BERUHIGEND</li></ul>
    <div class="medal">MIT<br>BIENEN-<br>WACHS</div>
    <p class="product product-line">Ohrenkerzen<br>LAVENDEL</p>
    <p class="tagline">Sinnliche Düfte für Harmonie<br>und Deine Entspannung</p>
    <div class="strip-bottom gold"></div>
  </section>
  <section class="pack pack--tone sandal" style="left:368px;top:105px">
    <div class="header gold"><span class="brand"><span class="brand-dot"></span>VelroMist</span></div>
    <ul class="tags"><li>ENTSPANNEND</li><li>BESINNLICH</li><li>BERUHIGEND</li></ul>
    <div class="medal">MIT<br>BIENEN-<br>WACHS</div>
    <p class="product product-line">Ohrenkerzen<br>SANDELHOLZ</p>
    <p class="tagline">Sinnliche Düfte für Harmonie<br>und Deine Entspannung</p>
    <div class="strip-bottom gold"></div>
  </section>

  <!-- Reihe 1: strukturierte Variante -->
  <section class="pack pack--tone pack--textured rose" style="left:561px;top:105px">
    <div class="header gold"><span class="brand"><span class="brand-dot"></span>VelroMist</span></div>
    <div class="ritual"><div class="ritual-title">Wellness-Ritual</div><ul><li>Entspannend</li><li>Besinnlich</li><li>Beruhigend</li></ul></div>
    <div class="medal">MIT<br>BIENEN-<br>WACHS</div>
    <p class="product product-line">Ohrenkerzen<br>ROSE</p>
    <p class="tagline">Sinnliche Düfte für Harmonie<br>und Deine Entspannung</p>
    <div class="strip-bottom gold"></div>
  </section>
  <section class="pack pack--tone pack--textured lavender" style="left:702px;top:105px">
    <div class="header gold"><span class="brand"><span class="brand-dot"></span>VelroMist</span></div>
    <div class="ritual"><div class="ritual-title">Wellness-Ritual</div><ul><li>Entspannend</li><li>Besinnlich</li><li>Beruhigend</li></ul></div>
    <div class="medal">MIT<br>BIENEN-<br>WACHS</div>
    <p class="product product-line">Ohrenkerzen<br>LAVENDEL</p>
    <p class="tagline">Sinnliche Düfte für Harmonie<br>und Deine Entspannung</p>
    <div class="strip-bottom gold"></div>
  </section>
  <section class="pack pack--tone pack--textured sandal" style="left:843px;top:105px">
    <div class="header gold"><span class="brand"><span class="brand-dot"></span>VelroMist</span></div>
    <div class="ritual"><div class="ritual-title">Wellness-Ritual</div><ul><li>Entspannend</li><li>Besinnlich</li><li>Beruhigend</li></ul></div>
    <div class="medal">MIT<br>BIENEN-<br>WACHS</div>
    <p class="product product-line">Ohrenkerzen<br>SANDELHOLZ</p>
    <p class="tagline">Sinnliche Düfte für Harmonie<br>und Deine Entspannung</p>
    <div class="strip-bottom gold"></div>
  </section>

  <!-- Reihe 2: Creme-Variante mit Duftmotiv -->
  <section class="pack pack--cream classic rose" style="left:87px;top:632px">
    <div class="strip-top gold"></div>
    <div class="cream-brand"><span class="brand brand--dark"><span class="brand-dot"></span>VelroMist</span></div>
    <h2 class="cream-title"><span class="kind">Ohrenkerzen</span><span class="scent">ROSE</span></h2>
    <div class="ritual"><div class="ritual-title">Wellness-Ritual</div><ul><li>Entspannend</li><li>Besinnlich</li><li>Beruhigend</li></ul></div>
    <div class="photo rose-photo" role="img" aria-label="Foto einer rosa Rosenblüte"></div>
    <div class="medal">MIT<br>BIENEN-<br>WACHS</div>
    <div class="footer gold">10 OHRENKERZEN</div>
  </section>
  <section class="pack pack--cream classic lavender" style="left:228px;top:632px">
    <div class="strip-top gold"></div>
    <div class="cream-brand"><span class="brand brand--dark"><span class="brand-dot"></span>VelroMist</span></div>
    <h2 class="cream-title"><span class="kind">Ohrenkerzen</span><span class="scent">LAVENDEL</span></h2>
    <div class="ritual"><div class="ritual-title">Wellness-Ritual</div><ul><li>Entspannend</li><li>Besinnlich</li><li>Beruhigend</li></ul></div>
    <div class="photo lavender-photo" role="img" aria-label="Foto eines blühenden Lavendelfelds"></div>
    <div class="medal">MIT<br>BIENEN-<br>WACHS</div>
    <div class="footer gold">10 OHRENKERZEN</div>
  </section>
  <section class="pack pack--cream classic sandal" style="left:368px;top:632px">
    <div class="strip-top gold"></div>
    <div class="cream-brand"><span class="brand brand--dark"><span class="brand-dot"></span>VelroMist</span></div>
    <h2 class="cream-title"><span class="kind">Ohrenkerzen</span><span class="scent">SANDELHOLZ</span></h2>
    <div class="ritual"><div class="ritual-title">Wellness-Ritual</div><ul><li>Entspannend</li><li>Besinnlich</li><li>Beruhigend</li></ul></div>
    <div class="photo sandal-photo" role="img" aria-label="Foto von Sandelholzstücken"></div>
    <div class="medal">MIT<br>BIENEN-<br>WACHS</div>
    <div class="footer gold">10 OHRENKERZEN</div>
  </section>

  <!-- Reihe 2: Creme-Variante mit Goldkopf -->
  <section class="pack pack--cream modern rose" style="left:561px;top:632px">
    <div class="header gold"><span class="brand"><span class="brand-dot"></span>VelroMist</span></div>
    <h2 class="cream-title"><span class="kind">Ohrenkerzen</span><span class="scent">Rose</span></h2>
    <div class="ritual"><div class="ritual-title">Wellness-Ritual</div><ul><li>Entspannend</li><li>Besinnlich</li><li>Beruhigend</li></ul></div>
    <div class="photo rose-photo" role="img" aria-label="Foto einer rosa Rosenblüte"></div>
    <div class="medal" style="top:168px">MIT<br>BIENEN-<br>WACHS</div>
    <div class="footer gold">10 OHRENKERZEN</div>
  </section>
  <section class="pack pack--cream modern lavender" style="left:702px;top:632px">
    <div class="header gold"><span class="brand"><span class="brand-dot"></span>VelroMist</span></div>
    <h2 class="cream-title"><span class="kind">Ohrenkerzen</span><span class="scent">Lavendel</span></h2>
    <div class="ritual"><div class="ritual-title">Wellness-Ritual</div><ul><li>Entspannend</li><li>Besinnlich</li><li>Beruhigend</li></ul></div>
    <div class="photo lavender-photo" role="img" aria-label="Foto eines blühenden Lavendelfelds"></div>
    <div class="medal" style="top:168px">MIT<br>BIENEN-<br>WACHS</div>
    <div class="footer gold">10 OHRENKERZEN</div>
  </section>
  <section class="pack pack--cream modern sandal" style="left:843px;top:632px">
    <div class="header gold"><span class="brand"><span class="brand-dot"></span>VelroMist</span></div>
    <h2 class="cream-title"><span class="kind">Ohrenkerzen</span><span class="scent">Sandelholz</span></h2>
    <div class="ritual"><div class="ritual-title">Wellness-Ritual</div><ul><li>Entspannend</li><li>Besinnlich</li><li>Beruhigend</li></ul></div>
    <div class="photo sandal-photo" role="img" aria-label="Foto von Sandelholzstücken"></div>
    <div class="medal" style="top:168px">MIT<br>BIENEN-<br>WACHS</div>
    <div class="footer gold">10 OHRENKERZEN</div>
  </section>

</main>
</body>
</html>
```